Modern home page design for insurance and investment business

- The design should be based around the attached HPID (home page information design) called KTW HPID. The table boxes are just for approximate placement of information – you DON'T have to make it look exactly like this.
- Information only is in orange text. Copy to go on the design in black text. Some instructions are in the HPID. Please be creative! You don’t have to use the exact images provided if you have a better idea.

- The design needs to be clean and spacious. Please use the colours from the logos in the website design. Lots of white too.

I've attached home page gallery example photos. You can use any of these photos or something similar with the words from one of the photos.

- Expected standard of design examples: (Please DO NOT copy these exactly – they are just examples)
http://www.harbourvane.co.nz/
https://www.brightkeel.co.nz/
http://sandorelcover.co.nz/homepage/

Width of content will be 1100 pixels when implemented as a web page. Header height (without nav bar) 150-160 pixels.

The winning PSD file will have to be provided as follows…
1. Canvas size of 2000px x 2000px - 72ppi in Adobe Photoshop (CS5 compatible)
2. Width of content section is 1100px wide - centered in the canvas
3. Any button rollovers/hovers in the PSD as hidden layers.
4. All fonts used must be Google fonts (except for the fonts in the header at the top of the page).
5. You will need to supply the chosen home page plus one example page (example page as a style guide for how all other pages will look). Example page is only the header and navigational bar at the top, an empty sector in the middle with a column (180 px wide) which can be left or right aligned which means the main sector is 920 pixels wide, and then the footer at the bottom of the page.

```html
<!DOCTYPE html>
<html lang="en">
<head>
<meta charset="utf-8">
<title>KTW Insure &amp; Invest</title>
<link href="https://fonts.googleapis.com/css2?family=Roboto:ital,wght@0,400;0,500;0,700;1,400&family=Bitter:ital,wght@1,700&display=swap" rel="stylesheet">
<style>
:root{
  --navy:#0b3d70;
  --grey-nav:#8d9aa6;
  --text:#222;
  --muted:#8a8f96;
  --page:#e8e8e8;
  --footer:#272727;
  --white:#fff;
}
*{box-sizing:border-box;margin:0;padding:0}
html,body{width:819px;height:1200px;overflow:hidden}
body{position:relative;font-family:"Roboto",Arial,sans-serif;color:var(--text);background:var(--page);font-size:8px}
.abs{position:absolute}
/* header */
.site-header{left:0;top:0;width:819px;height:100px;background:linear-gradient(#fff,#eeeeee)}
.brand{left:81px;top:36px;font:700 42px/1 "Roboto",sans-serif;color:var(--navy)}
.service-area{left:297px;top:15px;width:191px;height:73px;background:#dcdcd4}
.service-area .bar{height:20px;background:#9a9a9a;color:#fff;font-size:10px;line-height:20px;padding-left:9px}
.service-area .map{position:absolute;left:0;top:20px;width:191px;height:53px;background:linear-gradient(135deg,#e7e5dc,#d6d4c9)}
.service-area .label{position:absolute;left:76px;top:26px;width:82px;height:24px;background:#fff;border:1px solid #bbb;font-size:8px;line-height:10px;text-align:center;padding-top:2px}
.tagline{right:82px;top:28px;font:700 9px "Roboto",sans-serif;color:var(--navy)}
.subnav{right:82px;top:45px;font-size:9px;color:var(--muted)}
.phones{right:82px;top:61px;font:500 11px "Roboto",sans-serif;color:var(--navy);display:flex;align-items:center;gap:4px}
/* nav */
.main-nav{left:0;top:100px;width:819px;height:28px;background:var(--navy)}
.main-nav ul{list-style:none;display:flex;margin-left:81px;height:28px}
.main-nav li{color:#fff;font-size:10px;line-height:28px;padding:0 11px;border-right:1px solid #0a335d}
.main-nav li.active{background:var(--grey-nav)}
/* hero */
.hero{left:0;top:128px;width:819px;height:296px;background:linear-gradient(#8a6f3e 0%,#b8914f 35%,#7a6034 62%,#1a1710 78%,#050505 100%)}
.hero h1{position:absolute;left:81px;top:48px;font:italic 700 22px "Bitter",serif;color:#fff}
.hero .arrow{position:absolute;top:140px}
/* services */
.services{left:81px;top:424px;width:657px;height:162px;background:#fff}
.service{position:absolute;top:0;width:320px;text-align:center}
.service .ring{position:absolute;top:-32px;width:86px;height:86px;border-radius:50%;background:#fff;border:2px solid #ccc;padding:6px}
.service .ring .icon{width:100%;height:100%;border-radius:50%;background:radial-gradient(#dfe6ee,#c3cfdc)}
.service h2{position:absolute;top:64px;width:100%;font:500 12px "Roboto",sans-serif;color:var(--navy)}
.service p{position:absolute;top:84px;left:0;width:100%;font-size:7.5px;line-height:10.5px;color:#333}
.btn{display:inline-block;background:var(--navy);color:#fff;font:500 9px "Roboto",sans-serif;border-radius:2px}
.service .btn{position:absolute;top:121px;padding:4px 7px}
.divider{left:95px;top:586px;width:629px;height:1px;background:#bcbcbc}
.stages-title{left:0;top:603px;width:819px;text-align:center;font:700 12px "Roboto",sans-serif;color:var(--navy);display:flex;justify-content:center;gap:6px;align-items:center}
.card{top:637px;width:148px;height:213px;background:#fff;border-radius:6px;overflow:hidden;box-shadow:0 6px 8px rgba(0,0,0,.12)}
.card .photo{height:88px}
.card h3{text-align:center;font:700 12px "Roboto",sans-serif;color:var(--navy);text-decoration:underline;margin-top:6px}
.card ul{list-style:none;margin:6px 8px 0 22px;font-size:7.5px;line-height:9px;color:#333}
.card li{position:relative;margin-bottom:4px}
.card li::before{content:">";position:absolute;left:-11px}
.card .btn{position:absolute;left:37px;top:181px;width:72px;height:21px;text-align:center;line-height:21px;font-size:10px}
.form-title{left:0;top:874px;width:819px;text-align:center;font:700 12px "Roboto",sans-serif;color:var(--navy)}
.field{left:95px;width:309px;height:23px;background:#fff;border:1px solid #d4d4d4;border-radius:3px;font:italic 9px "Roboto",sans-serif;color:#333;padding:6px 8px}
.message{left:415px;top:906px;width:309px;height:82px;background:#fff;border:1px solid #d4d4d4;border-radius:3px;font:italic 9px "Roboto",sans-serif;padding:6px 9px}
.send{left:653px;top:995px;width:72px;height:24px;text-align:center;line-height:24px;font-size:12px;border-radius:3px}
/* footer */
.footer-bar{left:0;top:1037px;width:819px;height:29px;background:var(--navy)}
.footer-bar h4{position:absolute;top:8px;color:#fff;font:500 10px "Roboto",sans-serif}
.footer-body{left:0;top:1066px;width:819px;height:134px;background:var(--footer);color:#eee;font-size:7.5px;line-height:10.5px}
.footer-body ul{list-style:none;position:absolute}
.stage-links li{border-bottom:1px solid #555;padding:6px 0;width:106px}
.footer-body b{font-weight:700}
.foot-map{left:539px;top:10px;width:84px;height:76px;background:linear-gradient(135deg,#e4e2d8,#cfccc0)}
.copyright{left:81px;top:114px;font-weight:700}
.foot-rule{left:81px;top:101px;width:657px;height:1px;background:#444}
.social{right:82px;top:112px;display:flex;align-items:center;gap:5px}
.social .sq{width:12px;height:12px;background:#fff}
</style>
</head>
<body>
<header class="abs site-header">
  <div class="abs brand">KTW</div>
  <div class="abs service-area">
    <div class="bar">Servicing Clients New Zealand Wide</div>
    <div class="map" role="img" aria-label="Street map of the office location"></div>
    <div class="label">Located in sunny<br>Gisborne</div>
  </div>
  <div class="abs tagline">Smart Financial Decisions For Today And For Your Future</div>
  <div class="abs subnav">Insurances &nbsp;/&nbsp; Investments &nbsp;/&nbsp; Financial Planning</div>
  <div class="abs phones">
    <svg width="11" height="11" viewBox="0 0 12 12"><circle cx="6" cy="6" r="5.3" fill="none" stroke="#0b3d70"/><path d="M4 3.5l1 1-.6.8c.4.9 1 1.5 1.9 1.9l.8-.6 1 1-.8 1C5.5 8.4 3.6 6.5 3.4 4.3z" fill="#0b3d70"/></svg>
    0800 555 0147 &nbsp;|&nbsp; 06 555 0147
  </div>
</header>

<nav class="abs main-nav">
  <ul>
    <li class="active">Home</li><li>About</li><li>What We Do</li><li>What Life Stage are You?</li><li>Insurances</li><li>Investments</li><li>FAQs</li><li>Consultation</li><li>Contact/Map</li>
  </ul>
</nav>

<section class="abs hero" role="img" aria-label="Silhouette of a tractor in a field against a golden sunset sky">
  <h1>Planning for a Rainy day...</h1>
  <svg class="arrow" style="left:66px" width="12" height="18" viewBox="0 0 12 18"><path d="M10 2L3 9l7 7" fill="none" stroke="#3a3a3a" stroke-width="2.5"/></svg>
  <svg class="arrow" style="left:740px" width="12" height="18" viewBox="0 0 12 18"><path d="M2 2l7 7-7 7" fill="none" stroke="#3a3a3a" stroke-width="2.5"/></svg>
</section>

<section class="abs services">
  <div class="service" style="left:0">
    <div class="ring" style="left:113px"><div class="icon" role="img" aria-label="Illustration of a person holding an umbrella"></div></div>
    <h2>Insurance</h2>
    <p>An overview of insurance from the point of view of benefits to the customer of working with KTW will be in this space Relevant keywords such as the types of insurances e.g. life insurance, travel insurance etc will be mentioned...</p>
    <span class="btn" style="left:120px">Find Out More</span>
  </div>
  <div class="service" style="left:337px">
    <div class="ring" style="left:121px"><div class="icon" role="img" aria-label="Illustration of a person on a rising bar chart"></div></div>
    <h2>Investment</h2>
    <p>An overview of investments from the point of view of benefits to the customer of working with KTW will be in this space..... Relevant keywords such as financial planning, investment advice and NestSaver will be mentioned...</p>
    <span class="btn" style="left:130px">Find Out More</span>
  </div>
</section>
<div class="abs divider"></div>

<h2 class="abs stages-title">
  <svg width="18" height="13" viewBox="0 0 18 13"><circle cx="4" cy="2.5" r="2" fill="#0b3d70"/><circle cx="9" cy="4" r="1.8" fill="#0b3d70"/><circle cx="14" cy="2.5" r="2" fill="#0b3d70"/><rect x="2" y="5" width="4" height="8" fill="#0b3d70"/><rect x="7.5" y="6.5" width="3" height="6" fill="#0b3d70"/><rect x="12" y="5" width="4" height="8" fill="#0b3d70"/></svg>
  What Life Stage Are You At?
</h2>

<article class="abs card" style="left:81px">
  <div class="photo" role="img" aria-label="Young smiling couple" style="background:linear-gradient(135deg,#f1e7dc,#c99a7a)"></div>
  <h3>18-30 Years</h3>
  <ul><li style="color:#111">Should I Start Financial Planning Now?</li><li>What Insurances Do We Need?</li><li>What Is The Best Way To Save?</li></ul>
  <span class="btn">Learn More</span>
</article>
<article class="abs card" style="left:250px">
  <div class="photo" role="img" aria-label="Smiling family group outdoors" style="background:linear-gradient(#9cc36b,#6f9c4a)"></div>
  <h3>30-45 Years</h3>
  <ul><li>How do we create a balanced financial plan?</li><li>Have we got the right insurance cover?</li><li>Which investments are best for us?</li></ul>
  <span class="btn">Learn More</span>
</article>
<article class="abs card" style="left:420px">
  <div class="photo" role="img" aria-label="Couple embracing by the sea" style="background:linear-gradient(#6fa6d8,#1f5a92)"></div>
  <h3>45-65 Years</h3>
  <ul><li>Are we on track for retirement savings?</li><li>Is our health insurance cover enough?</li><li>Have we correctly structured our business?</li></ul>
  <span class="btn">Learn More</span>
</article>
<article class="abs card" style="left:589px">
  <div class="photo" role="img" aria-label="Retired couple at an outdoor table" style="background:linear-gradient(135deg,#e9e2c8,#b9ac7a)"></div>
  <h3>65+ Years</h3>
  <ul><li>Can we take our dream holiday?</li><li>Should we consider downsizing the house?</li><li>How often should we revise our will?</li></ul>
  <span class="btn">Learn More</span>
</article>

<h2 class="abs form-title">Would You Like KTW To Call You? Fill In The Form And We’ll Be In Touch…</h2>
<div class="abs field" style="top:906px">First Name:</div>
<div class="abs field" style="top:936px">Last Name:</div>
<div class="abs field" style="top:966px">Email:</div>
<div class="abs field" style="top:995px">Phone:</div>
<div class="abs message">Message:</div>
<span class="abs btn send">SEND</span>

<footer>
  <div class="abs footer-bar">
    <h4 style="left:81px">Quick Links</h4>
    <h4 style="left:210px">What Life Stage Are You?</h4>
    <h4 style="left:358px">Products/Services</h4>
    <h4 style="left:539px">Contact/Map</h4>
  </div>
  <div class="abs footer-body">
    <ul style="left:83px;top:8px"><li>Home</li><li>About</li><li>&gt; Meet the Team</li><li>&gt; Testimonials</li><li>What We Do</li><li>FAQs</li><li>Consultation</li></ul>
    <ul class="stage-links" style="left:210px;top:2px"><li>Life stage 18-30 years</li><li>Life stage 30-45 years</li><li>Life stage 45-65 years</li><li style="border-bottom:0">Life stage 65+ years</li></ul>
    <ul style="left:358px;top:8px"><li><b>Insurance</b></li><li>&gt; Life insurance</li><li>&gt; Trauma insurance</li><li>&gt; Disablement cover</li><li>&gt; Income protection</li><li style="margin-top:3px"><b>Investment</b></li><li>&gt; NestSaver</li></ul>
    <ul style="left:436px;top:18px"><li>&gt; Health insurance</li><li>&gt; Business insurance</li><li>&gt; Fire &amp; General</li><li>&gt; Travel insurance</li></ul>
    <div class="abs foot-map" role="img" aria-label="Small street map of the office"></div>
    <svg class="abs" style="left:629px;top:10px" width="12" height="15" viewBox="0 0 12 15"><path d="M6 0a6 6 0 0 1 6 6c0 4-6 9-6 9S0 10 0 6a6 6 0 0 1 6-6z" fill="#fff"/><circle cx="6" cy="6" r="2.2" fill="#272727"/></svg>
    <div class="abs" style="left:644px;top:9px">48 Harbour View Rd, Gisborne<br>New Zealand PO Box 4021,<br>Gisborne</div>
    <svg class="abs" style="left:630px;top:42px" width="11" height="11" viewBox="0 0 12 12"><circle cx="6" cy="6" r="5" fill="none" stroke="#fff" stroke-width="1.4"/><path d="M6 3v3h2.5" fill="none" stroke="#fff" stroke-width="1.2"/></svg>
    <div class="abs" style="left:644px;top:42px">Office Hours: 8.30 – 5pm<br>After Hours: Please phone:</div>
    <svg class="abs" style="left:630px;top:67px" width="11" height="11" viewBox="0 0 12 12"><circle cx="6" cy="6" r="5.3" fill="none" stroke="#fff"/><path d="M4 3.5l1 1-.6.8c.4.9 1 1.5 1.9 1.9l.8-.6 1 1-.8 1C5.5 8.4 3.6 6.5 3.4 4.3z" fill="#fff"/></svg>
    <div class="abs" style="left:644px;top:67px;font-weight:700">0800 555 0147<br>06 555 0147</div>
    <div class="abs foot-rule"></div>
    <div class="abs copyright">© 2014 KTW Investment | All Rights Reserved.</div>
    <div class="abs social"><span class="sq"></span><span>Chatterbook</span></div>
  </div>
</footer>
</body>
</html>
```